Harbourline Blinds & Shutters

It Needs to look classy as my target is the upper end of the blind market
I need a Logo design on front and description on back of what i do:
- Roller Blinds
- Vertical Blinds
- Venetian Blinds
- Plantation Shutters
- Aluminum External Shutters
and contact details
Declan
0418275063
and
Trent
0419852306
Updates
Hi Guys,
Sorry for the no feedback but i was waiting on my logo design. But its done now i have uploaded it. so if you could take a look and send through some designs
Reason: my logo was just finished an i just uploaded it today really dont understand why my deadline has been rached foe my bizcards as it states no deadline. But please extend
Target Market(s)
People that live on the coast and are looking for classy good quality blinds and shutters
Font styles to use
Other font styles liked:
- Copperplate Gothic,open to suggestion
Look and feel
Each slider illustrates characteristics of the customer's brand and the style your logo design should communicate.

```html
<!DOCTYPE html>
<html lang="en">
<head>
<meta charset="utf-8">
<title>Harbourline Blinds &amp; Shutters – Business Card</title>
<link rel="stylesheet" href="https://fonts.googleapis.com/css2?family=Marcellus&display=swap">
<style>
  :root {
    --page-bg: #ffffff;
    --card-edge: #0b0b0c;
    --card-glow: #2b2a31;
    --text-main: #f4f4f4;
    --brand-tone: #9a9aa0;
    --divider: rgba(235, 235, 240, 0.55);
  }
  html, body {
    margin: 0;
    width: 1200px;
    height: 1000px;
    overflow: hidden;
    background: var(--page-bg);
  }
  .business-card {
    position: absolute;
    left: 75px;
    top: 199px;
    width: 1050px;
    height: 603px;
    background: radial-gradient(ellipse 60% 65% at 55% 45%, var(--card-glow) 0%, #17171a 60%, var(--card-edge) 100%);
    font-family: "Marcellus", "Optima", sans-serif;
    color: var(--text-main);
  }
  .brand-name {
    position: absolute;
    left: 68px;
    top: 190px;
    width: 220px;
    margin: 0;
    font-size: 32px;
    font-weight: 400;
    line-height: 1.25;
    color: var(--brand-tone);
    letter-spacing: 0.5px;
  }
  .contact {
    position: absolute;
    top: 228px;
    margin: 0;
  }
  .contact-name {
    display: block;
    font-size: 41px;
    line-height: 48px;
  }
  .contact-phone {
    display: block;
    font-size: 43px;
    line-height: 52px;
    letter-spacing: 1px;
  }
  .contact--first { left: 297px; }
  .contact--second { left: 737px; }
  .contact-divider {
    position: absolute;
    left: 647px;
    top: 200px;
    width: 1.5px;
    height: 198px;
    background: linear-gradient(to bottom, transparent, var(--divider) 30%, var(--divider) 70%, transparent);
  }
  .services {
    position: absolute;
    left: 68px;
    top: 480px;
    margin: 0;
    font-size: 38px;
    line-height: 50px;
    white-space: nowrap;
  }
</style>
</head>
<body>
  <section class="business-card">
    <h1 class="brand-name">Harbourline Blinds &amp; Shutters</h1>

    <p class="contact contact--first">
      <span class="contact-name">Declan</span>
      <span class="contact-phone">0418275063</span>
    </p>

    <div class="contact-divider"></div>

    <p class="contact contact--second">
      <span class="contact-name">Trent</span>
      <span class="contact-phone">0419852306</span>
    </p>

    <p class="services">
      Roller Blinds | Vertical Blinds | Venetian Blinds<br>
      Plantation Shutters | Aluminum External Shutters
    </p>
  </section>
</body>
</html>
```